Turn Photo into Graphic Design Image for Home Page

We need to take a photo and create a graphic image for our home page. We are currently using a monochrome (green) cut out version of the attached photo. (see www.belvintorlegal.example) We are creating a new website, but would like to use the same photo, but with a background (either texture, or a skyline of Austin). I am open to manipulating the photo and background in any way you want to try (although don't keep the current background). It doesn't have to be green, although that is our current branding. It doesn't have to be monochrome either. Basically, I'd like to see what you come up with. I'd like to design to be cool/edgy. It can be minimal. It needs to be modern. It needs to be the dimensions of a webpage (rectangular). With the person (me) on the right hand side. In the same position as the belvintorlegal.example page.

Requirements
Should not have
• The image should not have any text on it.

```html
<!DOCTYPE html>
<html lang="en">
<head>
<meta charset="utf-8">
<title>The Law Office of Morgan Belvintor</title>
<link href="https://fonts.googleapis.com/css2?family=Lato:wght@300;400;700;900&display=swap" rel="stylesheet">
<style>
:root{
  --green:#1c8a2e;
  --green-dark:#136b22;
  --ink:#444;
  --muted:#8a8a8a;
  --icon:#9a9a9a;
  --band:#ececec;
  --page:#ffffff;
  --star:#c8242c;
}
*{margin:0;padding:0;box-sizing:border-box}
html,body{width:1200px;height:750px;overflow:hidden;background:var(--page);font-family:"Lato",sans-serif;color:var(--ink)}
.page{position:relative;width:1200px;height:750px;overflow:hidden;background:var(--page)}
.main-nav{position:absolute;top:38px;left:300px;display:flex;gap:8px;font-size:11px;color:var(--ink)}
.main-nav a{color:inherit;text-decoration:none}
.main-nav a.active{color:var(--green);font-weight:700}
.main-nav .sep{color:#bbb}
.header-contact{position:absolute;top:32px;left:930px;font-size:12px;line-height:18px}
.header-contact .phone{color:var(--green);font-weight:700;display:flex;align-items:center;gap:6px}
.header-contact .pay{color:var(--muted);font-weight:900;font-size:10px;letter-spacing:1px;display:flex;align-items:center;gap:6px}
.header-contact svg{width:12px;height:12px}
.title-block{position:absolute;top:215px;left:200px;width:400px}
.title-kicker{font-weight:300;color:var(--green);font-size:18px;letter-spacing:.3px;line-height:22px}
.title-name{font-weight:900;color:var(--green-dark);font-size:36px;line-height:40px;letter-spacing:-.5px;white-space:nowrap}
.title-city{text-align:right;font-size:10px;color:var(--muted);margin-top:2px}
.practice{position:absolute;top:345px;left:235px}
.practice-lead{font-size:10px;color:var(--muted);font-style:italic;margin-bottom:12px}
.practice-list{display:flex;gap:16px;list-style:none}
.practice-item{width:46px;text-align:center;font-size:8px;line-height:10px;color:var(--muted)}
.practice-item svg{width:38px;height:38px;display:block;margin:0 auto 6px}
.hero-photo{position:absolute;top:120px;left:690px;width:420px;height:420px;border-radius:50%;
  background:radial-gradient(circle at 50% 45%,#c98f86 0%,#b7a8a2 45%,#d9d4d2 70%,rgba(255,255,255,0) 72%)}
.review-band{position:absolute;top:520px;left:0;width:1200px;height:230px;background:var(--band)}
.quote-mark{position:absolute;top:-16px;left:568px;width:32px;height:32px;border-radius:50%;background:#fff;border:1px solid #ddd;color:var(--muted);font-weight:900;font-size:20px;text-align:center;line-height:34px}
.review{position:absolute;top:50px;left:250px;display:flex;gap:22px;align-items:flex-start}
.review-badge{width:54px;height:54px;background:#fff;box-shadow:0 1px 3px rgba(0,0,0,.2);display:flex;align-items:center;justify-content:center}
.review-badge span{display:block;width:40px;height:10px;background:var(--star)}
.review-text{width:260px;font-size:10px;line-height:14px;color:var(--muted);font-style:italic}
.carousel-dots{position:absolute;top:150px;left:565px;display:flex;gap:5px}
.carousel-dots i{width:6px;height:6px;border-radius:50%;background:#c6c6c6}
.carousel-dots i.on{background:#999}
.office{position:absolute;top:50px;left:740px;width:230px;text-align:right;font-size:12px;line-height:16px;color:var(--ink);font-style:normal}
.office-name{color:var(--green);font-weight:700}
.office-phone{color:var(--green);font-weight:700;margin-top:6px}
.office-fax{font-weight:700}
.office-fax small{font-weight:400;font-size:9px;color:var(--muted)}
</style>
</head>
<body>
<div class="page">
  <nav class="main-nav">
    <a class="active" href="#">Home</a><span class="sep">|</span>
    <a href="#">Areas of Practice</a><span class="sep">|</span>
    <a href="#">About</a><span class="sep">|</span>
    <a href="#">FAQ</a><span class="sep">|</span>
    <a href="#">Reviews</a><span class="sep">|</span>
    <a href="#">Videos</a><span class="sep">|</span>
    <a href="#">DWI eBook</a><span class="sep">|</span>
    <a href="#">Contact</a>
  </nav>

  <div class="header-contact">
    <div class="phone"><svg viewBox="0 0 12 12"><rect width="12" height="12" rx="2" fill="#9a9a9a"/><path d="M3.5 2.8l1.3 1.2-.6 1a5 5 0 0 0 2.8 2.8l1-.6 1.2 1.3-.9 1C5.6 9.2 2.8 6.4 2.5 3.7z" fill="#fff"/></svg>(555) 014-2210</div>
    <div class="pay"><svg viewBox="0 0 12 12"><rect width="12" height="12" rx="2" fill="#9a9a9a"/><rect x="2.5" y="4" width="7" height="4.5" fill="#fff"/></svg>PAY ONLINE</div>
  </div>

  <div class="title-block">
    <div class="title-kicker">THE LAW OFFICE OF</div>
    <div class="title-name">MORGAN BELVINTOR</div>
    <div class="title-city">Austin, TX</div>
  </div>

  <section class="practice">
    <p class="practice-lead">Practice areas of focus</p>
    <ul class="practice-list">
      <li class="practice-item"><svg viewBox="0 0 40 40"><circle cx="20" cy="20" r="19" fill="var(--icon)"/><rect x="11" y="17" width="18" height="8" rx="2" fill="#fff"/><path d="M14 17l2-5h8l2 5z" fill="#fff"/><circle cx="15" cy="26" r="2" fill="#fff"/><circle cx="25" cy="26" r="2" fill="#fff"/></svg>DWI</li>
      <li class="practice-item"><svg viewBox="0 0 40 40"><circle cx="20" cy="20" r="19" fill="var(--icon)"/><path d="M15 19v-4a5 5 0 0 1 10 0" stroke="#fff" stroke-width="2.5" fill="none"/><rect x="12" y="19" width="16" height="11" rx="2" fill="#fff"/></svg>Theft</li>
      <li class="practice-item"><svg viewBox="0 0 40 40"><circle cx="20" cy="20" r="19" fill="var(--icon)"/><path d="M20 9c5 6 5 12 0 18c-5-6-5-12 0-18z" fill="#fff"/><path d="M20 27v5" stroke="#fff" stroke-width="2"/></svg>Marijuana / Drugs</li>
      <li class="practice-item"><svg viewBox="0 0 40 40"><circle cx="20" cy="20" r="19" fill="var(--icon)"/><circle cx="14" cy="21" r="5" stroke="#fff" stroke-width="2.5" fill="none"/><circle cx="26" cy="21" r="5" stroke="#fff" stroke-width="2.5" fill="none"/><path d="M19 17h2" stroke="#fff" stroke-width="2"/></svg>Assault</li>
      <li class="practice-item"><svg viewBox="0 0 40 40"><circle cx="20" cy="20" r="19" fill="var(--icon)"/><rect x="13" y="10" width="14" height="20" rx="1" fill="#fff"/><path d="M16 15h8M16 19h8M16 23h6" stroke="var(--icon)" stroke-width="1.5"/></svg>Warrants &amp; Jail Release</li>
      <li class="practice-item"><svg viewBox="0 0 40 40"><circle cx="20" cy="20" r="19" fill="var(--icon)"/><circle cx="20" cy="20" r="10" stroke="#fff" stroke-width="2.5" fill="none"/><path d="M14 14l12 12M26 14L14 26" stroke="#fff" stroke-width="2.5"/></svg>Other Misdemeanors &amp; Felonies</li>
    </ul>
  </section>

  <div class="review-band">
    <div class="quote-mark">&ldquo;</div>
    <div class="review">
      <div class="review-badge"><span></span></div>
      <p class="review-text">Morgan was professional and responsive. He explained every step clearly and got a result I did not expect. Highly recommend.</p>
    </div>
    <div class="carousel-dots"><i></i><i class="on"></i><i></i><i></i></div>
    <address class="office">
      <div class="office-name">Law Office of Morgan Belvintor</div>
      <div>418 Linden Street</div>
      <div>Austin, Texas 78700</div>
      <div class="office-phone">(555) 014-2210</div>
      <div class="office-fax"><small>FAX</small> (555) 014-2290</div>
      <div>contact@belvintorlegal.example</div>
    </address>
  </div>

  <div class="hero-photo" role="img" aria-label="Portrait of the attorney in a suit holding a briefcase, set against a warm-toned Austin skyline inside a soft circular frame"></div>
</div>
</body>
</html>
```